New Infographic Design Project

I need a 1 page Infographic that explains our Quillstone Prism offer.

Can you use the following content in the attached document to create a 1 page infographic. The image in the bottom of the document is one of our competitors who is offering the same thing, this image is only provided for inspiration and ideas as we need ours to be based on the content of the document and aligned with the Corvenly Brand

```html
<!DOCTYPE html>
<html lang="en">
<head>
<meta charset="utf-8">
<title>Corvenly – Data Ready, AI Ready in 6 Weeks</title>
<link href="https://fonts.googleapis.com/css2?family=Rubik:wght@400;500;600;700&display=swap" rel="stylesheet">
<style>
:root{
  --bg:#0a0c1c;
  --band:#0c1450;
  --red:#d8192b;
  --red-text:#e3202f;
  --blue:#3148d8;
  --blue-deep:#1a2a9e;
  --blue-text:#4a62ff;
  --white:#ffffff;
  --line:#22306e;
  --card:#0c1245;
}
*{margin:0;padding:0;box-sizing:border-box}
html,body{width:1200px;height:1003px;overflow:hidden;background:var(--bg)}
body{font-family:"Rubik",sans-serif;color:var(--white);position:relative}
.abs{position:absolute}
.brand{left:0;width:1200px;top:18px;text-align:center;font-size:60px;font-weight:600;letter-spacing:-1px;line-height:1}
.brand .mark{display:inline-block;width:34px;height:34px;border:4px solid var(--red);border-radius:50%;vertical-align:top;margin-left:6px;margin-top:2px}
.band{left:0;top:157px;width:1200px;height:162px;background:var(--band)}
.chev{position:absolute;top:127px;height:64px;display:flex;align-items:center;justify-content:center;font-weight:600;font-size:42px;
  clip-path:polygon(0 0,calc(100% - 34px) 0,100% 50%,calc(100% - 34px) 100%,0 100%,34px 50%)}
.chev.c1{left:70px;width:373px;background:var(--blue)}
.chev.c2{left:419px;width:375px;background:var(--blue-deep)}
.chev.c3{left:771px;width:370px;background:var(--red)}
.tagline{left:70px;top:207px;font-size:30px;font-weight:700;color:var(--red-text)}
.intro{left:70px;top:250px;width:720px;font-size:16px;font-weight:500;line-height:23px}
.partner{left:842px;top:217px;display:flex;align-items:center;gap:14px;font-size:26px;font-weight:400}
.partner .sq{width:58px;height:62px;background:linear-gradient(135deg,#3ee0a0,#0f7a6a)}
.section{left:70px;font-size:30px;font-weight:700;color:var(--red-text);background:var(--bg);padding-right:18px}
.rule{left:0;width:1200px;height:1px;background:var(--line)}
.edge-card{top:378px;height:125px;border:1.5px solid;border-radius:8px;padding:12px 10px 0 32px}
.edge-card.red{border-color:var(--red)}
.edge-card.blue{border-color:var(--blue)}
.edge-card h3{font-size:18px;font-weight:600;line-height:18px}
.edge-card.red h3{color:var(--red-text)}
.edge-card.blue h3{color:var(--blue-text)}
.edge-card p{font-size:12.5px;line-height:15.5px;margin-top:4px}
.dot{position:absolute;left:-18px;top:30px;width:38px;height:38px;border-radius:50%;background:var(--bg);display:flex;align-items:center;justify-content:center}
.red .dot{border:2px solid var(--red);box-shadow:0 0 8px var(--red)}
.blue .dot{border:2px solid var(--blue);box-shadow:0 0 8px var(--blue)}
.week{position:absolute;top:567px;height:53px;display:flex;align-items:center;justify-content:center;font-size:26px;font-weight:700;
  clip-path:polygon(0 0,calc(100% - 22px) 0,100% 50%,calc(100% - 22px) 100%,0 100%,22px 50%)}
.week.r{background:linear-gradient(180deg,#e01f30,#9b0f1c)}
.week.b{background:linear-gradient(180deg,#2137c8,#121f86)}
.step{position:absolute;top:638px;width:162px}
.step h4{font-size:12.5px;font-weight:600;line-height:16px;text-transform:uppercase}
.step.r h4{color:var(--red-text)}
.step.b h4{color:var(--blue-text)}
.step p{font-size:12.5px;line-height:15.5px;margin-top:3px}
.divider{position:absolute;top:638px;width:1px;height:200px;background:var(--line)}
.extra{position:absolute;top:830px;height:106px;background:var(--card);border-radius:8px;padding:12px 10px 0 38px;box-shadow:0 0 10px rgba(40,60,200,.35)}
.extra h4{font-size:12.5px;font-weight:600;color:var(--red-text);line-height:13.5px;text-transform:uppercase}
.extra p{font-size:12.5px;line-height:15.5px;margin-top:3px}
.sqicon{position:absolute;left:-16px;top:26px;width:40px;height:44px;border-radius:7px;display:flex;align-items:center;justify-content:center}
.sqicon.r{background:var(--red)}
.sqicon.b{background:var(--blue)}
</style>
</head>
<body>
<div class="abs brand">corvenly<span class="mark"></span></div>

<div class="abs band"></div>
<div class="chev c1">Data Ready</div>
<div class="chev c2">AI Ready</div>
<div class="chev c3">In 6 Weeks</div>

<div class="abs tagline">Your long-term strategic data partner</div>
<p class="abs intro">We start with a Business Data Assessment or Prism Deployment Assessment to pinpoint the highestvalue use cases, the biggest data risks, and the fastest path to impact.</p>
<div class="abs partner"><span class="sq"></span>Quillstone Prism</div>

<div class="abs rule" style="top:348px"></div>
<div class="abs section" style="top:328px">The Corvenly Edge</div>

<div class="abs edge-card red" style="left:82px;width:242px">
  <span class="dot"><svg width="20" height="20" viewBox="0 0 20 20" fill="none" stroke="#fff" stroke-width="1.6"><circle cx="10" cy="10" r="7"/><path d="M6.5 10l2.5 2.5 4.5-5"/></svg></span>
  <h3>Quality-first delivery</h3>
  <p>Automated validation, data tests, and “quality gates” that stop bad data upstream.</p>
</div>
<div class="abs edge-card blue" style="left:350px;width:244px">
  <span class="dot"><svg width="20" height="20" viewBox="0 0 20 20" fill="none" stroke="#fff" stroke-width="1.6"><circle cx="10" cy="10" r="7"/><circle cx="10" cy="10" r="3"/></svg></span>
  <h3>Data products, not datasets</h3>
  <p>Clear ownership, SLAs, versioning, and reusable, consumable outputs aligned to high impact business outcomes.</p>
</div>
<div class="abs edge-card red" style="left:617px;width:243px">
  <span class="dot"><svg width="20" height="20" viewBox="0 0 20 20" fill="none" stroke="#fff" stroke-width="1.6"><path d="M3 8l7-4 7 4M4 16h12M6 9v6M10 9v6M14 9v6"/></svg></span>
  <h3>Governance that doesn’t slow you down</h3>
  <p>Security, access, lineage, and auditability built in from day one.</p>
</div>
<div class="abs edge-card blue" style="left:886px;width:243px">
  <span class="dot"><svg width="20" height="20" viewBox="0 0 20 20" fill="none" stroke="#fff" stroke-width="1.6"><circle cx="8.5" cy="8.5" r="5"/><path d="M12.5 12.5l4.5 4.5"/></svg></span>
  <h3>Operate seamlessly</h3>
  <p>CI/CD, monitoring, and cost controls so the platform stays healthy.</p>
</div>

<div class="abs rule" style="top:542px"></div>
<div class="abs section" style="top:522px">6 week time to value</div>

<div class="week r" style="left:66px;width:184px">WEEK 1</div>
<div class="week b" style="left:241px;width:169px">WEEK 2</div>
<div class="week r" style="left:417px;width:183px">WEEK 3</div>
<div class="week b" style="left:592px;width:183px">WEEK 4</div>
<div class="week r" style="left:769px;width:182px">WEEK 5</div>
<div class="week b" style="left:944px;width:183px">WEEK 6</div>

<div class="step r" style="left:74px"><h4>Envision &amp; Assess</h4><p>Use case shortlist and priority based on highest business impact, current-state review, data risk &amp; compliance priorities, target operating model.</p></div>
<div class="divider" style="left:239px;height:110px"></div>
<div class="step b" style="left:246px"><h4>Architecture &amp;<br>Governance Design</h4><p>Landing zone decisions, security and access model, patterns/ standards, delivery plan and success metrics.</p></div>
<div class="divider" style="left:412px;height:110px"></div>
<div class="step r" style="left:419px"><h4>Prism Foundation<br>Deployed</h4><p>Workspaces and environments, automation &amp; CI/CD, onboarding playbooks, baseline policies/guardrails.</p></div>
<div class="divider" style="left:587px;height:110px"></div>
<div class="step b" style="left:594px;width:176px"><h4>Data Ingestion +<br>Validation Framework</h4><p>Reusable ingestion patterns, automated validation, data contracts/ SLAs, observability signals and alerting.</p></div>
<div class="divider" style="left:771px;height:110px"></div>
<div class="step r" style="left:777px"><h4>Scalable Common<br>Data Model</h4><p>Domain model, master entities, curated layer, semantic modelling patterns that support Lumaview BI at scale.</p></div>
<div class="divider" style="left:945px;height:110px"></div>
<div class="step b" style="left:951px;width:178px"><h4>Business Outcomes +<br>AI-Ready Capability</h4><p>Executive dashboards and priority reports, performance optimisation, hypercare and handover, AI readiness check and pilot plan (predictive analytics and/or secure enterprise LLM).</p></div>

<div class="abs rule" style="top:796px"></div>
<div class="abs section" style="top:776px">Extra Edge</div>

<div class="extra" style="left:87px;width:237px">
  <span class="sqicon r"><svg width="24" height="24" viewBox="0 0 24 24" fill="none" stroke="#fff" stroke-width="1.7"><circle cx="12" cy="12" r="8"/><path d="M8 12l3 3 5-6"/></svg></span>
  <h4>“AI-Ready Data” Guarantee</h4>
  <p>Every priority dataset ships with validation rules, ownership, lineage, and freshness SLAs before it can power AI.</p>
</div>
<div class="extra" style="left:350px;width:238px">
  <span class="sqicon b"><svg width="24" height="24" viewBox="0 0 24 24" fill="none" stroke="#fff" stroke-width="1.7"><rect x="5" y="3" width="12" height="16" rx="1"/><path d="M8 8h6M8 11h6M8 14h3"/><circle cx="16" cy="16" r="3"/><path d="M18 18l3 3"/></svg></span>
  <h4>Cost-to-Serve<br>Transparency</h4>
  <p>Show business owners what each product/ report costs to run and optimise it continuously.</p>
</div>
<div class="extra" style="left:615px;width:237px">
  <span class="sqicon r"><svg width="24" height="24" viewBox="0 0 24 24" fill="none" stroke="#fff" stroke-width="1.7"><rect x="5" y="3" width="14" height="18" rx="1"/><path d="M8 13l3 3 5-6"/></svg></span>
  <h4>Change-Proof Pipelines</h4>
  <p>Data contracts + automated tests reduce breakages from upstream schema changes.</p>
</div>
<div class="extra" style="left:889px;width:238px">
  <span class="sqicon b"><svg width="24" height="24" viewBox="0 0 24 24" fill="none" stroke="#fff" stroke-width="1.7"><path d="M4 9l8-5 8 5M5 20h14M7 10v8M10.5 10v8M13.5 10v8M17 10v8"/></svg></span>
  <h4>Governed Self-Serve</h4>
  <p>Catalog + certified datasets so teams move faster without creating data chaos.</p>
</div>
</body>
</html>
```